Wine and retail website for a high-end resort community

We are introducing a line of quality wines in the resort community of Martha's Vineyard, Massachusetts, USA. The site will detail information about the wine, and online store connected to and external government approved shipper for wine, and additional non-alcoholic retail merchandise sales.

We are planning the site to be driven off the Squarespace platform so I do not believe coding is necessary initially; however, the ability to do sop would be helpful if needed.

Attached are the images/files we have available so far. Please feel free to use stock images in your design.

Target Market(s)

Wine enthusiasts in the resort community of Martha’s Vineyard Massachusetts

Industry/Entity Type

Wine

Number of Pages Required

4 page

Font styles to use
Sans Serif

Requirements
Must have
• Home page, about page, wine page, e-commerce page, retail merchandise page. I recently came across brelmorcellars.com and really like the look and layout of their pages if that helps
Nice to have
• A short wine/Martha’s Vineyard related video on the home page

```html
<!DOCTYPE html>
<html lang="en">
<head>
<meta charset="utf-8">
<title>Seagrass Point Estates</title>
<link href="https://fonts.googleapis.com/css2?family=Fira+Sans:wght@400;600;700;800&family=Open+Sans:wght@400;600;700&display=swap" rel="stylesheet">
<style>
:root{
  --crimson:#b71f3d;
  --red:#d0102e;
  --pink:#ee4d65;
  --pink-deep:#dc2740;
  --frame:#e0304f;
  --ink:#111;
  --white:#fff;
  --amber:#c9832e;
  --brown:#3a1f10;
}
*{box-sizing:border-box;margin:0;padding:0}
html,body{width:1200px;height:2646px;overflow:hidden;background:var(--white);font-family:"Open Sans",sans-serif}
.page{position:relative;width:1200px;height:2646px;overflow:hidden}
.hero{position:absolute;left:0;top:0;width:1200px;height:760px}
.topbar{position:absolute;left:0;top:0;width:1200px;height:74px;background:var(--crimson);z-index:3}
.nav{position:absolute;right:78px;top:27px;display:flex;gap:13px;align-items:center;font-size:13px;color:var(--white)}
.nav a{color:inherit;text-decoration:none}
.nav .active{color:var(--ink);font-weight:700}
.brand-box{position:absolute;left:65px;top:36px;width:226px;height:170px;background:var(--white);border:2px solid #ddd;z-index:4;display:flex;align-items:center;justify-content:center;text-align:center;font-family:"Fira Sans",sans-serif;font-weight:700;font-size:30px;line-height:1.05;color:#333}
.hero-copy{position:absolute;left:129px;top:258px;z-index:3;color:var(--white)}
.hero-title{font-family:"Fira Sans",sans-serif;font-weight:800;font-size:44px;line-height:54px;letter-spacing:1px;text-transform:uppercase}
.hero-sub{margin-top:32px;font-family:"Fira Sans",sans-serif;font-weight:700;font-size:24px;line-height:29px;width:540px;text-shadow:2px 2px 2px rgba(0,0,0,.6)}
.btn-order{position:absolute;left:131px;top:499px;width:241px;height:34px;border-radius:17px;background:var(--crimson);color:var(--white);font-family:"Fira Sans",sans-serif;font-weight:700;font-size:24px;line-height:34px;text-align:center;z-index:3}
.island-map{position:absolute;left:503px;top:622px;width:175px;height:108px;border-radius:40% 50% 30% 45%;background:linear-gradient(135deg,#555,#111)}
.section-title{position:absolute;left:0;width:1200px;text-align:center;font-family:"Fira Sans",sans-serif;font-weight:800;font-variant:small-caps;color:var(--red);font-size:42px}
.intro{position:absolute;left:205px;top:808px;width:790px;text-align:center;font-size:13px;line-height:15.5px;color:var(--crimson)}
.video{position:absolute;left:339px;top:912px;width:521px;height:300px;border:8px solid var(--frame);border-radius:6px;background:radial-gradient(circle at 50% 60%,#6a1020 0,#3a1a3a 25%,#4c7a20 60%,#8fbf3a 100%)}
.card-back{position:absolute;background:var(--ink)}
.card{position:absolute;background:linear-gradient(105deg,var(--pink-deep) 0,var(--pink-deep) 12%,#e33451 40%,var(--pink) 100%);color:var(--white)}
.photo{position:absolute;background:radial-gradient(ellipse at 50% 55%,#2a2a2a 0,#000 70%)}
.wine-name{font-family:"Fira Sans",sans-serif;font-weight:800;font-size:21px;color:var(--ink);text-transform:uppercase;letter-spacing:.5px}
.wine-region{font-family:"Fira Sans",sans-serif;font-weight:700;font-size:22px;color:var(--white)}
.wine-text{font-size:13px;line-height:15.5px;margin-top:12px}
.warn-title{font-family:"Fira Sans",sans-serif;font-weight:700;font-size:16px;text-decoration:underline;margin-top:18px}
.warn b{font-size:15px}
.sulfites{font-family:"Fira Sans",sans-serif;font-weight:700;font-size:12px;margin-top:14px}
.volume{font-size:15px;margin-top:14px}
.btn-cart{position:absolute;width:240px;height:34px;border-radius:17px;background:var(--white);color:var(--ink);font-size:24px;line-height:34px;text-align:center}
.footer{position:absolute;left:0;top:2592px;width:1200px;height:54px;background:var(--pink-deep);color:var(--white);font-size:13px;text-align:center;line-height:54px}
</style>
</head>
<body>
<div class="page">
  <header class="topbar">
    <nav class="nav">
      <a class="active">Home</a><a>About Us</a><a>Contact</a><a>Order Now</a>
      <svg width="20" height="20" viewBox="0 0 20 20" fill="none" stroke="#fff" stroke-width="1.4"><path d="M1 3h3l2 10h10l2-7H5"/><circle cx="8" cy="17" r="1.4"/><circle cx="15" cy="17" r="1.4"/></svg>
    </nav>
  </header>
  <div class="brand-box">Seagrass<br>Point<br>Estates</div>

  <svg class="hero" viewBox="0 0 1200 760" role="img" aria-label="Close-up photo of white and red wine glasses in warm light">
    <defs>
      <linearGradient id="heroBg" x1="0" y1="0" x2="1" y2="0">
        <stop offset="0" stop-color="#5a2d12"/><stop offset=".35" stop-color="#c9832e"/><stop offset=".6" stop-color="#e8c27a"/><stop offset=".85" stop-color="#7a3a14"/><stop offset="1" stop-color="#2a1408"/>
      </linearGradient>
      <linearGradient id="fade" x1="0" y1="0" x2="0" y2="1">
        <stop offset="0" stop-color="#b71f3d"/><stop offset=".45" stop-color="#e7a2b0"/><stop offset="1" stop-color="#fff"/>
      </linearGradient>
    </defs>
    <rect width="1200" height="700" fill="url(#heroBg)"/>
    <path d="M0 650 C150 700 300 660 450 620 C600 580 720 585 880 610 C1020 630 1120 620 1200 610 V760 H0 Z" fill="url(#fade)"/>
  </svg>

  <div class="hero-copy">
    <h1 class="hero-title">Seagrass Point<br>Estates</h1>
    <p class="hero-sub">The 58th largest island in the U.S and now introducing Wines</p>
  </div>
  <div class="btn-order">Order Online!</div>

  <div class="island-map" role="img" aria-label="Silhouette map of the island"></div>

  <h2 class="section-title" style="top:740px">Seagrass Point Estates</h2>
  <p class="intro">Lorem Ipsum is simply dummy text of the printing and typesetting industry. Lorem Ipsum has been the industry's standard dummy text ever since the 1500s, when an unknown printer took a galley of type and scrambled it to make a type specimen book. It has survived not only five centuries, but also the leap into electronic typesetting, remaining essentially unchanged. It was popularised in the 1960s with the release of Lettercraft sheets containing Lorem Ipsum passages, and more recently with desktop publishing software like PageForge including versions of Lorem Ipsum.</p>

  <div class="video" role="img" aria-label="Video of a glass of red wine in front of grape vines"></div>

  <h2 class="section-title" style="top:1262px">Buy Now Online</h2>

  <!-- Chardonnay -->
  <div class="card-back" style="left:421px;top:1361px;width:697px;height:553px"></div>
  <div class="card" style="left:393px;top:1331px;width:697px;height:553px">
    <div style="position:absolute;left:143px;top:54px;width:450px">
      <div class="wine-name">Chardonnay</div>
      <div class="wine-region" style="margin-left:119px">California</div>
      <p class="wine-text">Seagrass Point Estates Chardonnay is defined by an array of fragrant fruit with buttery undertones that finish long and smooth. A true classic that is sure to please any palate.</p>
      <p class="wine-text" style="margin-top:16px">We hope our wines are a reminder of good times and good company spent on the Vineyard. Here's to keeping it on island time!</p>
      <p class="warn-title">GOVERNMENT WARNING:</p>
      <p class="wine-text warn" style="margin-top:18px"><b>(1)</b> According to the Surgeon General, women should not drink alcoholic beverages during pregnancy because of the risk of birth defects.</p>
      <p class="wine-text warn" style="margin-top:16px"><b>(2)</b> Consumption of alcoholic beverages impairs your ability to drive a car or operate machinery, and may cause health problems.</p>
      <p class="sulfites">CONTAINS SULFITES</p>
      <p class="volume">750 mL (25.35 oz) ALC. 14.5% BY VOL</p>
    </div>
    <div class="btn-cart" style="left:406px;top:378px">Add to Cart</div>
  </div>
  <div class="photo" style="left:65px;top:1366px;width:400px;height:489px;border-radius:60px 0 60px 0" role="img" aria-label="Photo of a red and a white wine bottle on black"></div>

  <!-- Cabernet -->
  <div class="card-back" style="left:86px;top:2001px;width:676px;height:536px"></div>
  <div class="card" style="left:110px;top:1972px;width:677px;height:534px">
    <div style="position:absolute;left:73px;top:80px;width:440px">
      <div class="wine-name">Cabernet Sauvignon</div>
      <div class="wine-region" style="margin-left:224px">California</div>
      <p class="wine-text">Seagrass Point Estates Cabernet Sauvignon shows aromas of oak, baking spice, and cassis. On the palate, tones of black cherry and a hint of cinnamon, nutmeg and French Vanilla leave a delicious lasting finish.</p>
      <p class="wine-text" style="margin-top:16px">We hope our wines are a reminder of good times and good company spent on the Vineyard. Here's to keeping it on island time!</p>
      <p class="warn-title">GOVERNMENT WARNING:</p>
      <p class="wine-text warn" style="margin-top:18px"><b>(1)</b> According to the Surgeon General, women should not drink alcoholic beverages during pregnancy because of the risk of birth defects.</p>
      <p class="wine-text warn" style="margin-top:16px"><b>(2)</b> Consumption of alcoholic beverages impairs your ability to drive a car or operate machinery, and may cause health problems.</p>
      <p class="sulfites">CONTAINS SULFITES</p>
      <p class="volume">750 mL (25.35 oz) ALC. 14.5% BY VOL</p>
    </div>
    <div class="btn-cart" style="left:346px;top:412px">Add to Cart</div>
  </div>
  <div class="photo" style="left:734px;top:1997px;width:400px;height:489px;border-radius:60px 0 60px 0" role="img" aria-label="Photo of a red and a white wine bottle on black"></div>

  <footer class="footer">@Copyright <b>Seagrass Point Estates.</b> All Rights Reserved.</footer>
</div>
</body>
</html>
```